Kestly HVAC Services - High end letter head, Quote Template & Invoice Template

Provide word documents for the below.
- Letterhead for emails & letters.
- Quote template (similar to the attached)
- Invoice template (similar to the attached)
Logo colours should be used.
Modern, bold, professional look.
Kestly Logo - Voruma Specialist Dealer logo - Contact information

See attachments of previously used documents.

Target Market(s)

High end clients

Industry/Entity Type

Air Conditioning & Mechanical Ventilation (HVAC)

Font styles to use
Sans Serif
Other font styles liked:
• Arial Narrow or similar - Text similar to the KESTLY logo

Requirements
Must have
• Kestly Logo - Voruma Specialist Dealer logo - Contact information
Nice to have
• Logo colours used throughout the documents
Should not have
• Bright colours, yellow, pink, green etc

```html
<!DOCTYPE html>
<html lang="en">
<head>
<meta charset="utf-8">
<title>Kestly HVAC Services – Stationery Set</title>
<link rel="stylesheet" href="https://fonts.googleapis.com/css2?family=Open+Sans:wght@400;500;600;700;800&display=swap">
<style>
:root{
  --canvas:#ebebeb;
  --paper:#ffffff;
  --ink:#1b1b1b;
  --black:#000000;
  --blue:#1a86d6;
  --blue-light:#5fb3ea;
  --panel:#efefef;
  --row:#ececec;
  --red:#d8232a;
}
*{margin:0;padding:0;box-sizing:border-box}
html,body{width:1200px;height:575px;overflow:hidden;background:var(--canvas)}
body{position:relative;font-family:"Open Sans",Arial,sans-serif;color:var(--ink)}
.page{position:absolute;top:32px;width:351px;height:496px;background:var(--paper);box-shadow:0 2px 6px rgba(0,0,0,.18);overflow:hidden}
.page--letter{left:34px}
.page--invoice{left:422px}
.page--quote{left:809px}
.doc-label{position:absolute;top:544px;width:351px;text-align:center;font-size:11px;letter-spacing:1.6px;color:#333}
.abs{position:absolute}
.r{text-align:right}

/* header band */
.masthead{position:absolute;left:0;top:0;width:351px;height:60px}
.brand{position:absolute;left:24px;top:18px;display:flex;align-items:center;gap:4px}
.brand-mark{width:9px;height:9px;background:var(--blue)}
.brand-name{font-weight:800;font-size:15px;color:#fff;letter-spacing:.5px;line-height:1}
.brand-tag{position:absolute;left:24px;top:40px;font-size:3.6px;color:#fff;letter-spacing:.2px;white-space:nowrap}
.contact{position:absolute;right:24px;top:12px;font-size:7.2px;line-height:10.6px;text-align:right;color:var(--ink)}
.contact b{font-weight:600}

/* letterhead */
.lt{font-size:7.3px;line-height:8.6px}
.letter-body{position:absolute;left:26px;top:213px;width:301px}
.body-copy{font-size:6.85px;line-height:9.4px;text-align:justify;letter-spacing:-.05px;margin-bottom:9.4px}
.sign-off{font-size:7.3px;line-height:9.4px}
.footer-bar{position:absolute;left:26px;top:475px;width:300px;height:.8px;background:#444}
.copyright{position:absolute;left:0;width:351px;top:480px;text-align:center;font-size:4.6px;color:#333}

/* invoice */
.doc-title{position:absolute;left:25px;top:82px;font-size:18.5px;font-weight:500;letter-spacing:.2px}
.client-box{position:absolute;left:25px;top:117px;width:302px;height:37px;background:var(--panel)}
.client-name{position:absolute;left:8px;top:5px;font-size:7.3px}
.client-sub{position:absolute;left:8px;top:14px;font-size:5.6px;line-height:7px}
.client-fields{position:absolute;left:150px;top:5px;font-size:7.2px;line-height:9.4px}
.tbl-head{position:absolute;height:17px;color:#fff;font-size:7.3px;display:flex;align-items:center;justify-content:center}
.th-blue{background:var(--blue)}
.th-black{background:var(--black)}
.tbl-cell{position:absolute;background:var(--row)}
.totals{position:absolute;font-size:7.2px;line-height:10.6px}
.value-rule{position:absolute;height:.6px;background:#333}
.divider{position:absolute;height:.7px;background:#555}
.pay{font-size:7.3px;line-height:10.6px}
.pay b{font-weight:600}
.icon-slot{position:absolute;background:#f2f2f2;border-radius:6px}
.footer-rule{position:absolute;left:25px;width:302px;top:472px;height:.5px;background:#777}
.footer-title{position:absolute;left:0;width:351px;top:469.5px;text-align:center;font-size:4.4px;font-weight:600;color:var(--red)}
.footer-title span{background:#fff;padding:0 3px}
.footer-line{position:absolute;left:0;width:351px;text-align:center;font-size:4.3px;color:#222;white-space:nowrap}

/* quote */
.q-brand{position:absolute;left:25px;top:18px;display:flex;align-items:center;gap:4px}
.q-brand .brand-name{color:var(--blue);font-size:16px}
.q-brand .brand-mark{width:10px;height:10px}
.dealer{position:absolute;right:25px;top:20px;font-size:12px;font-weight:800;color:var(--blue);letter-spacing:.3px;white-space:nowrap}
.fine-head{position:absolute;left:25px;font-size:4.5px;font-weight:700;display:flex;align-items:center;width:300px;gap:3px}
.fine-head i{flex:1;height:.4px;background:#666}
.fine{position:absolute;left:25px;width:301px;font-size:4.25px;line-height:7px;text-align:left}
.sign-slot{position:absolute;left:25px;top:221px;width:46px;height:13px;background:linear-gradient(90deg,#f1f1f1,#e3e3e3)}
</style>
</head>
<body>

<!-- LETTERHEAD -->
<section class="page page--letter">
  <svg class="masthead" viewBox="0 0 351 60" aria-hidden="true">
    <rect width="351" height="60" fill="var(--panel)"/>
    <path d="M0 0H139C163 0 170 42 199 60H0Z" fill="var(--black)"/>
    <path d="M139 0C163 0 170 42 199 60" fill="none" stroke="var(--blue)" stroke-width="3"/>
    <path d="M143 0C167 0 175 42 205 60" fill="none" stroke="var(--blue-light)" stroke-width="1.2"/>
  </svg>
  <div class="brand"><span class="brand-mark"></span><span class="brand-name">KESTLY</span></div>
  <div class="brand-tag">| HEATING | VENTILATION | AIR CONDITIONING |</div>
  <div class="contact">
    <div><b>Phone:</b> +0412 555 187</div>
    <div><b>Email:</b> rhys@kestlyhvac.com.au</div>
    <div><b>ABN:</b> 51 604 223 908</div>
    <div><b>Lic No.</b> 218834C ARC No. AU51723.</div>
  </div>

  <div class="abs lt" style="left:26px;top:104px">To,</div>
  <div class="abs lt r" style="right:24px;top:104px">30-08-2023</div>
  <div class="abs lt" style="left:26px;top:126px">John Doe<br>Designation</div>
  <div class="abs lt" style="left:26px;top:154px">P: (123)456-789<br>E: info@example.com</div>
  <div class="abs lt" style="left:25px;top:187px">Respected Sir/Ma’am,</div>

  <div class="letter-body">
    <p class="body-copy">Lorem ipsum dolor sit amet, consectetur adipiscing elit, sed do eiusmod tempor incididunt ut labore et dolore magna aliqua. Ut enim ad minim veniam, quis nostrud exercitation ullamco laboris nisi ut aliquip ex ea commodo consequat. Duis aute irure dolor in reprehenderit in voluptate velit esse cillum dolore eu fugiat nulla pariatur. Excepteur sint occaecat cupidatat non proident, sunt in culpa qui officia deserunt mollit anim id est laborum.</p>
    <p class="body-copy">Sed ut perspiciatis unde omnis iste natus error sit voluptatem accusantium doloremque laudantium, totam rem aperiam, eaque ipsa quae ab illo inventore veritatis et quasi architecto beatae vitae dicta sunt explicabo. Nemo enim ipsam voluptatem quia voluptas sit aspernatur aut odit aut fugit, sed quia consequuntur magni dolores eos qui ratione voluptatem sequi nesciunt. Neque porro quisquam est, qui dolorem ipsum quia dolor sit amet, consectetur, adipisci velit, sed quia non numquam eius modi tempora incidunt ut labore et dolore magnam aliquam quaerat voluptatem. Ut enim ad minima veniam, quis nostrum exercitationem ullam corporis suscipit laboriosam, nisi ut aliquid ex ea commodi consequatur? Quis autem vel eum iure reprehenderit qui in ea voluptate velit esse quam nihil molestiae consequatur, vel illum qui dolorem eum fugiat quo voluptas nulla pariatur?</p>
    <p class="body-copy">Lorem ipsum dolor sit amet, consectetur adipiscing elit, sed do eiusmod tempor incididunt ut labore et dolore magna aliqua. Ut enim ad minim veniam, quis nostrud exercitation ullamco laboris nisi ut aliquip ex ea commodo consequat.</p>
    <p class="sign-off">Your Sincerely,</p>
  </div>

  <svg class="abs" style="left:212px;top:467px" width="115" height="9" viewBox="0 0 115 9" aria-hidden="true">
    <path d="M4 0H115V9H0Z" fill="var(--blue)"/>
  </svg>
  <div class="footer-bar"></div>
  <div class="copyright">Copyright © 2023 Kestly HVAC</div>
</section>
<div class="doc-label" style="left:34px">LETTERHEAD</div>

<!-- TAX INVOICE -->
<section class="page page--invoice">
  <svg class="masthead" viewBox="0 0 351 60" aria-hidden="true">
    <rect width="351" height="60" fill="var(--panel)"/>
    <path d="M0 0H139C163 0 170 42 199 60H0Z" fill="var(--black)"/>
    <path d="M139 0C163 0 170 42 199 60" fill="none" stroke="var(--blue)" stroke-width="3"/>
    <path d="M143 0C167 0 175 42 205 60" fill="none" stroke="var(--blue-light)" stroke-width="1.2"/>
  </svg>
  <div class="brand"><span class="brand-mark"></span><span class="brand-name">KESTLY</span></div>
  <div class="brand-tag">| HEATING | VENTILATION | AIR CONDITIONING |</div>
  <div class="contact">
    <div><b>Phone:</b> +0412 555 187</div>
    <div><b>Email:</b> rhys@kestlyhvac.com.au</div>
    <div><b>ABN:</b> 51 604 223 908</div>
    <div><b>Lic No.</b> 218834C ARC No. AU51723.</div>
  </div>

  <h1 class="doc-title">TAX INVOICE</h1>
  <div class="abs r" style="right:24px;top:85px;font-size:7.3px;line-height:10.6px">Wednesday 30<sup style="font-size:4px">th</sup> August 2023<br>Invoice number: 1111</div>

  <div class="client-box">
    <div class="client-name">Company Name</div>
    <div class="client-sub">Lorem ipsum dolor sit amet,<br>consectetur adipiscing elit,</div>
    <div class="client-fields">Address:<br>Phone:<br>Email:</div>
  </div>

  <div class="tbl-head th-blue" style="left:25px;top:165px;width:29px">SL No:</div>
  <div class="tbl-head th-blue" style="left:55px;top:165px;width:163px">Description</div>
  <div class="tbl-head th-black" style="left:220px;top:165px;width:53px">Unit Price</div>
  <div class="tbl-head th-black" style="left:275px;top:165px;width:52px">Amount</div>

  <div class="tbl-cell" style="left:25px;top:183px;width:29px;height:19px"></div>
  <div class="tbl-cell" style="left:55px;top:183px;width:163px;height:19px"></div>
  <div class="tbl-cell" style="left:220px;top:183px;width:53px;height:19px"></div>
  <div class="tbl-cell" style="left:275px;top:183px;width:52px;height:19px"></div>

  <div class="tbl-cell" style="left:25px;top:222px;width:29px;height:19px"></div>
  <div class="tbl-cell" style="left:55px;top:222px;width:163px;height:19px"></div>
  <div class="tbl-cell" style="left:220px;top:222px;width:53px;height:19px"></div>
  <div class="tbl-cell" style="left:275px;top:222px;width:52px;height:19px"></div>

  <div class="tbl-cell" style="left:25px;top:261px;width:29px;height:19px"></div>
  <div class="tbl-cell" style="left:55px;top:261px;width:163px;height:19px"></div>
  <div class="tbl-cell" style="left:220px;top:261px;width:53px;height:19px"></div>
  <div class="tbl-cell" style="left:275px;top:261px;width:52px;height:19px"></div>

  <div class="tbl-cell" style="left:25px;top:298px;width:29px;height:19px"></div>
  <div class="tbl-cell" style="left:55px;top:298px;width:163px;height:19px"></div>
  <div class="tbl-cell" style="left:220px;top:298px;width:53px;height:19px"></div>
  <div class="tbl-cell" style="left:275px;top:298px;width:52px;height:19px"></div>

  <div class="totals" style="left:208px;top:324px">Current Claim<br>GST<br>Total (Inc GST</div>
  <div class="totals" style="left:273px;top:323px">$0,000.00<br>$&nbsp;&nbsp;000.00<br>$0,000.00</div>
  <div class="value-rule" style="left:273px;top:333px;width:54px"></div>
  <div class="value-rule" style="left:273px;top:344px;width:54px"></div>

  <div class="divider" style="left:25px;top:362px;width:300px"></div>

  <div class="abs pay" style="left:25px;top:367px"><b>How to pay</b></div>
  <div class="abs pay" style="left:71px;top:367px">By Electronic Funds<br>transfer (EFT)</div>
  <div class="icon-slot" style="left:25px;top:383px;width:36px;height:19px" role="img" aria-label="Computer mouse icon"></div>

  <div class="abs pay" style="left:208px;top:375px">Invoice Number<br>Total Due<br>Due Date</div>
  <div class="abs pay" style="left:273px;top:375px">1111<br>$0,000.00<br>07-09-2023</div>

  <div class="abs pay" style="left:25px;top:412px"><b>Bank:</b><br><b>Acc. Name:</b><br><b>BSB:</b><br><b>Acc. No.</b></div>
  <div class="abs pay" style="left:70px;top:412px">Harbourline Bank<br>Kestly HVAC Services<br>000 000<br>0000 0000 0000</div>

  <div class="footer-rule"></div>
  <div class="footer-title"><span>KESTLY HVAC SERVICES PTY LTD</span></div>
  <div class="footer-line" style="top:477px">PO Box 41 Calderton, NSW 2190 | Mobile: 0412 555 187 | Email: rhys@kestlyhvac.com.au | Web: www.kestlyhvac.com.au |</div>
  <div class="footer-line" style="top:484px">ABN: 51 604 223 908 | Licence No: 218834C | ARC No: AU51723</div>
</section>
<div class="doc-label" style="left:422px">TAX INVOICE</div>

<!-- QUOTATION -->
<section class="page page--quote">
  <div class="q-brand"><span class="brand-mark"></span><span class="brand-name">KESTLY</span></div>
  <div class="dealer">VORUMA SPECIALIST DEALER</div>

  <div class="abs" style="left:26px;top:49px;font-size:7.2px;line-height:10.6px">Name:<br>Address:<br>Phone:<br>Email:</div>
  <div class="abs r" style="right:25px;top:49px;font-size:7.2px;line-height:10.6px">05/09/2023<br>Quote No: 1111<br>Valid Till: 30 Days</div>
  <div class="divider" style="left:25px;top:95px;width:301px"></div>

  <div class="abs" style="left:0;width:351px;top:103px;text-align:center;font-size:7.3px;font-weight:600">Air Conditioning &amp; Mechanical Ventilation Proposal for ______________</div>
  <p class="abs" style="left:25px;width:302px;top:116px;font-size:7px;line-height:9.3px;text-align:justify">Thank you for the opportunity to provide a quotation for the above-mentioned address. If you have any questions regarding the items listed below, please do not hesitate to contact me directly.</p>

  <div class="tbl-head th-blue" style="left:25px;top:151px;width:29px">SL No:</div>
  <div class="tbl-head th-blue" style="left:55px;top:151px;width:200px">Description</div>
  <div class="tbl-head th-black" style="left:256px;top:151px;width:70px">Amount</div>
  <div class="tbl-cell" style="left:25px;top:169px;width:29px;height:19px"></div>
  <div class="tbl-cell" style="left:55px;top:169px;width:200px;height:19px"></div>
  <div class="tbl-cell" style="left:256px;top:169px;width:70px;height:19px"></div>

  <div class="abs" style="left:206px;top:196px;font-size:7.2px">Total (Inc GST</div>
  <div class="abs" style="left:270px;top:195px;font-size:7.2px">$0,000.00</div>

  <div class="abs" style="left:25px;top:210px;font-size:7.3px">Kindly Regards</div>
  <div class="sign-slot" role="img" aria-label="Handwritten signature"></div>
  <div class="abs" style="left:26px;top:238px;font-size:7.2px;line-height:10.7px">Rhys Kestly<br>0412 555 187<br>rhys@kestlyhvac.com.au<br>www.kestlyhvac.com.au</div>

  <div class="fine-head" style="top:287px">General Exclusions <i></i></div>
  <div class="fine" style="top:294px">1. Any core holes, chasing or large masonry penetrations. (unless specified otherwise)<br>2. Any craneage or vertical lifting of the air conditioning equipment.<br>3. Cutting out of and supply and installation of any access panels required for future servicing and warranty work.<br>4. And cutting and framing of walls or bulkheads required for the installation of the system.<br>5. Power supply to the condensers. (unless specified otherwise)<br>6. Upgrading of the existing power supply to the main switchboard.<br>7. Any acoustic treatment to the condensing unit.<br>8. Any additional builders works. This includes all patching and painting works.<br>9. Applying for any permits including council or strata approval.</div>

  <div class="fine-head" style="top:365px">Payment Terms <i></i></div>
  <div class="fine" style="top:372px">A 20% deposit will be required on ordering of the system. Payment terms are strictly 7 days from the day of completion or on receiving a progress claim for an ongoing project.<br>Payments can be made by EFT direct transfer, cheque cash or credit card. (payments by standard credit cards incur an additional 1.5% fee and premium charge cards 2%)</div>

  <div class="fine-head" style="top:408px">Warranty <i></i></div>
  <div class="fine" style="top:415px">• All Voruma air conditioning units installed in domestic applications come with a 5 year warranty. This includes wall mounted split systems, ducted systems, cassette systems and multi-zone systems.<br>• Commercial multi-zone installations come with a 1 year warranty.<br>• All systems that are not installed for human comfort come with out a warranty.<br>• All condensate pumps (unless they are supplied with the Voruma system) come with a 6 month warranty.<br>• All zone motors come with a 1 year warranty.<br>• Access is required to the underside of all inbuilt systems. If additional access to the systems is required for repair works it is not covered under the warranty.</div>

  <div class="divider" style="left:25px;top:473px;width:301px;height:.5px"></div>
  <div class="footer-line" style="top:477px">9 / 120-128 Ashgrove Road, Calderton | Ph: 0412 555 187 | E: rhys@kestlyhvac.com.au | Web: www.kestlyhvac.com.au</div>
  <div class="footer-line" style="top:484px">ABN: 51 604 223 908 | Licence No: 218834C | ARC No: AU51723</div>
</section>
<div class="doc-label" style="left:809px">QUOTATION</div>

</body>
</html>
```